Job Coaching - Vanta; engaging people to improve their work experience

I need a flyer for Job Coaching. It serves to engage customers (not businesses) with problems in their daily job, typical questions that are handled are:
Do I fit for the job?
Am I using my talents at best in this job?
I have a conflict with my manager/colleagues, what should I do?
My work-life balance is a mess, how can I improve this?
What job fits best with my talents?
I'm getting stressed out from my job, what can I do?
....
This Flyer will be available at GP's, therpeutic practices, pharamcists,...
this flyer should put people in action to contact me
Flyer can be created in English, in the final one the text should be in Dutch; I will make the translation of the selected flyer and provide it at the end

Target Market(s)

consumers / customers / people having a job, but somewhat stuck in it

Industry/Entity Type

Professional Coaching

Requirements
Must have
• the questions mentioned in the project description; mobile number: 0471/389145; email: tom.vermeer@vantacoaching.example; website: www.vantacoaching.example ; it should make also reference to 'Career guidance cheques of the KWOL'

```html
<!DOCTYPE html>
<html lang="en">
<head>
<meta charset="utf-8">
<title>Career Guidance – Vanta Job Coaching</title>
<link rel="stylesheet" href="https://fonts.googleapis.com/css2?family=Montserrat:wght@500;600;700;800;900&family=Open+Sans:wght@400;600;700&display=swap">
<style>
  :root {
    --teal: #3aa89c;
    --teal-dark: #2b8c82;
    --slate: #6b6d70;
    --slate-dark: #3f4245;
    --ink: #4a4d50;
    --paper: #ffffff;
    --backdrop: #e4e5e6;
    --photo-a: #b8443f;
    --photo-b: #d9a98d;
  }
  * { box-sizing: border-box; margin: 0; padding: 0; }
  html, body { width: 672px; height: 1200px; overflow: hidden; }
  body { background: var(--backdrop); font-family: "Open Sans", Arial, sans-serif; }

  .flyer {
    position: absolute; left: 16px; top: 16px;
    width: 640px; height: 1168px;
    background: var(--paper);
    overflow: hidden;
    box-shadow: 0 2px 10px rgba(0,0,0,.15);
  }

  /* Header */
  .masthead { position: absolute; left: 0; top: 28px; width: 100%; text-align: center; }
  .masthead__title {
    font-family: "Montserrat", Arial, sans-serif; font-weight: 900;
    color: var(--teal); font-size: 104px; line-height: 92px; letter-spacing: 1px;
  }
  .masthead__sub {
    font-family: "Montserrat", Arial, sans-serif; font-weight: 600;
    color: var(--ink); font-size: 20px; margin-top: 8px;
  }
  .intro {
    position: absolute; left: 40px; right: 40px; top: 260px;
    text-align: center; font-family: "Montserrat", Arial, sans-serif;
    font-weight: 800; color: var(--slate-dark); font-size: 21px; line-height: 27px;
    text-transform: uppercase;
  }

  /* Body */
  .body-panel { position: absolute; left: 0; top: 340px; width: 640px; height: 680px; background: var(--slate); }

  .questions {
    position: absolute; left: 18px; top: 330px; width: 290px; height: 690px;
    background: var(--teal); padding: 24px 20px 0 22px; color: var(--paper);
  }
  .questions__lead {
    font-family: "Montserrat", Arial, sans-serif; font-weight: 800;
    font-size: 17px; line-height: 22px; text-transform: uppercase; margin-bottom: 16px;
  }
  .questions__list { list-style: none; }
  .questions__item {
    display: flex; gap: 10px; align-items: flex-start;
    font-family: "Montserrat", Arial, sans-serif; font-weight: 700;
    font-size: 14px; line-height: 18px; margin-bottom: 11px;
  }
  .questions__item svg { flex: 0 0 18px; margin-top: 0; }

  .together {
    position: absolute; left: 18px; top: 810px; width: 200px; height: 124px;
  }
  .together__text {
    position: absolute; left: 0; top: 18px; width: 172px; text-align: center;
    font-family: "Montserrat", Arial, sans-serif; font-weight: 900;
    color: var(--paper); font-size: 18px; line-height: 22px;
  }

  .story {
    position: absolute; left: 330px; top: 360px; width: 290px; color: #eef0f0;
    font-size: 11.5px; line-height: 17px;
  }
  .story p { margin-bottom: 12px; }
  .story__callout {
    font-family: "Montserrat", Arial, sans-serif; font-weight: 800; color: var(--paper);
    text-align: right; font-size: 16px; line-height: 21px; text-transform: uppercase;
    margin: 10px 0 20px 60px;
  }
  .story__cheques {
    text-align: right; font-family: "Montserrat", Arial, sans-serif;
    font-weight: 700; color: var(--paper); font-size: 15px;
  }
  .partner {
    display: flex; justify-content: flex-end; align-items: center; gap: 10px; margin-top: 8px;
  }
  .partner__mark { width: 22px; height: 22px; background: var(--paper); }
  .partner__name {
    font-family: "Montserrat", Arial, sans-serif; font-weight: 900;
    color: var(--paper); font-size: 46px; line-height: 46px;
  }

  .portrait {
    position: absolute; left: 236px; top: 790px; width: 210px; height: 230px;
    background: linear-gradient(180deg, var(--photo-b) 0%, #c98a72 45%, var(--photo-a) 100%);
  }

  /* Footer */
  .footer {
    position: absolute; left: 0; top: 1020px; width: 640px; height: 148px;
    background: var(--paper); border-top: 6px solid var(--teal);
  }
  .brand { position: absolute; left: 32px; top: 44px; display: flex; align-items: center; gap: 12px; }
  .brand__dot { width: 34px; height: 34px; border-radius: 50%; background: var(--teal); }
  .brand__name {
    font-family: "Montserrat", Arial, sans-serif; font-weight: 900;
    color: var(--teal); font-size: 44px; line-height: 44px;
  }
  .contact { position: absolute; right: 28px; top: 24px; text-align: right; }
  .contact__phone {
    display: flex; align-items: center; justify-content: flex-end; gap: 10px;
    font-family: "Montserrat", Arial, sans-serif; font-weight: 800;
    color: var(--teal); font-size: 44px; line-height: 52px;
  }
  .contact__line { color: var(--ink); font-size: 13px; line-height: 20px; font-weight: 600; }
</style>
</head>
<body>
<main class="flyer">
  <header class="masthead">
    <h1 class="masthead__title">CAREER<br>GUIANCE</h1>
    <p class="masthead__sub">(with Career Vouchers)</p>
  </header>
  <p class="intro">During this career counseling, we take<br>a close look at your personalsituation.</p>

  <div class="body-panel"></div>

  <section class="questions">
    <h2 class="questions__lead">Do you recognize your self in any of the following questions?</h2>
    <ul class="questions__list">
      <li class="questions__item"><svg width="18" height="18" viewBox="0 0 20 20"><circle cx="10" cy="10" r="10" fill="#fff"/><path d="M6 10h7M10 6l4 4-4 4" stroke="#3aa89c" stroke-width="2.4" fill="none" stroke-linecap="round" stroke-linejoin="round"/></svg>Do you know who you want, but do not dare to take the step?</li>
      <li class="questions__item"><svg width="18" height="18" viewBox="0 0 20 20"><circle cx="10" cy="10" r="10" fill="#fff"/><path d="M6 10h7M10 6l4 4-4 4" stroke="#3aa89c" stroke-width="2.4" fill="none" stroke-linecap="round" stroke-linejoin="round"/></svg>How can I work better with my manager and/ or colleagues?</li>
      <li class="questions__item"><svg width="18" height="18" viewBox="0 0 20 20"><circle cx="10" cy="10" r="10" fill="#fff"/><path d="M6 10h7M10 6l4 4-4 4" stroke="#3aa89c" stroke-width="2.4" fill="none" stroke-linecap="round" stroke-linejoin="round"/></svg>I'm getting stressed out from my job, what can I do?</li>
      <li class="questions__item"><svg width="18" height="18" viewBox="0 0 20 20"><circle cx="10" cy="10" r="10" fill="#fff"/><path d="M6 10h7M10 6l4 4-4 4" stroke="#3aa89c" stroke-width="2.4" fill="none" stroke-linecap="round" stroke-linejoin="round"/></svg>Am I using my talents at best in this job?</li>
      <li class="questions__item"><svg width="18" height="18" viewBox="0 0 20 20"><circle cx="10" cy="10" r="10" fill="#fff"/><path d="M6 10h7M10 6l4 4-4 4" stroke="#3aa89c" stroke-width="2.4" fill="none" stroke-linecap="round" stroke-linejoin="round"/></svg>How can I get a better work- life balance?</li>
      <li class="questions__item"><svg width="18" height="18" viewBox="0 0 20 20"><circle cx="10" cy="10" r="10" fill="#fff"/><path d="M6 10h7M10 6l4 4-4 4" stroke="#3aa89c" stroke-width="2.4" fill="none" stroke-linecap="round" stroke-linejoin="round"/></svg>What are my talents?</li>
    </ul>
  </section>

  <div class="together">
    <svg width="200" height="124" viewBox="0 0 200 124"><path d="M0 0H165L200 62L165 124H0Z" fill="#3f4245"/></svg>
    <p class="together__text">THEN WE<br>WILL WORK ON<br>THIS<br>TOGETHER.</p>
  </div>

  <section class="story">
    <p>We really want to take our time for this process. In four sessions we look at your needs, your wishes and your options. Together we make a clear plan with steps you can take right away at work.</p>
    <p>In addition, we listen to what gives you energy and what drains it. Based on that we explore your strengths and your values, so that your next move feels right.</p>
    <p style="margin-left:110px">Unfortunately, not every person can afford this. That is why you can use career vouchers to cover most of the cost.</p>
    <p class="story__callout">And that's where career counseling comes into play...</p>
    <p class="story__cheques">Career guidance cheques of the</p>
    <div class="partner"><span class="partner__mark"></span><span class="partner__name">KWOL</span></div>
  </section>

  <div class="portrait" role="img" aria-label="Portrait photo of the coach"></div>

  <footer class="footer">
    <div class="brand"><span class="brand__dot"></span><span class="brand__name">Vanta</span></div>
    <div class="contact">
      <div class="contact__phone">
        <svg width="34" height="34" viewBox="0 0 24 24"><path d="M6.6 10.8a15 15 0 0 0 6.6 6.6l2.2-2.2a1 1 0 0 1 1-.25 11.4 11.4 0 0 0 3.6.57 1 1 0 0 1 1 1V20a1 1 0 0 1-1 1A17 17 0 0 1 3 4a1 1 0 0 1 1-1h3.5a1 1 0 0 1 1 1c0 1.25.2 2.45.57 3.6a1 1 0 0 1-.25 1z" fill="#3aa89c"/></svg>
        0471/389145
      </div>
      <p class="contact__line">tom.vermeer@vantacoaching.example</p>
      <p class="contact__line">www.vantacoaching.example</p>
    </div>
  </footer>
</main>
</body>
</html>
```